I would like to modify/update my 2 step login screen

I want a more modern looking login page for our document imaging application. I need to keep all of the same elements and buttons that currently exist. The first 2 screens are the login. The 3rd is a screenshot of the actual application home page.

```html
<!DOCTYPE html>
<html lang="en">
<head>
<meta charset="utf-8">
<title>Classic Login – Sign-in Flow</title>
<link href="https://fonts.googleapis.com/css2?family=Inter:wght@400;500;600;700&display=swap" rel="stylesheet">
<style>
:root{
  --page:#f0f0f0;
  --charcoal:#3b3c3e;
  --surface:#fafafa;
  --card:#ffffff;
  --ink:#2b2b2b;
  --muted:#8a8a8a;
  --line:#dcdcdc;
  --green:#5cb85c;
  --blue:#4a7fd6;
  --red:#e05555;
  --disabled:#c9c9c9;
  --chip:#f1f1f1;
}
*{box-sizing:border-box;margin:0;padding:0}
html,body{width:1200px;height:482px;overflow:hidden;background:var(--page);font-family:Inter,sans-serif;color:var(--ink)}
.board{position:relative;width:1200px;height:482px}
.screen{position:absolute;width:371px;height:209px;background:var(--surface);overflow:hidden}
.screen-header{height:59px;background:var(--charcoal)}
.brand{position:absolute;top:15px;left:0;right:0;text-align:center;color:#fff;font-weight:700;font-size:6px;letter-spacing:.6px}
.card{position:absolute;left:99px;top:41.5px;width:174px;background:var(--card);border-radius:2px;box-shadow:0 .5px 2px rgba(0,0,0,.14)}
.tabs{display:flex;height:17px;border-bottom:.5px solid #ececec}
.tab{flex:1;display:flex;align-items:center;justify-content:center;position:relative}
.tab.active::after{content:"";position:absolute;left:0;right:0;bottom:-.5px;height:1.2px;background:var(--green)}
.tab-dot{width:5.5px;height:5.5px;border-radius:50%;background:#9aa0a6}
.tab-square{width:5px;height:5px;background:#9aa0a6}
.tab-dot.dark{background:#111}
.card-body{position:relative}
.step-one .card-body{height:69.5px}
.step-two .card-body{height:102.5px}
.title{position:absolute;left:17.5px;top:10px;font-weight:600;font-size:6.6px}
.error{position:absolute;right:17.5px;top:12px;font-size:2.8px;color:var(--red)}
.field{position:absolute;left:17.5px;width:139px;height:14.5px;border:.5px solid var(--line);border-radius:8px;background:#fff}
.field.focused{border:.7px solid var(--blue)}
.field.invalid{border:.7px solid var(--red)}
.field-icon{position:absolute;left:1.8px;top:1.5px;width:10.5px;height:10.5px;border-radius:50%;background:var(--chip);display:flex;align-items:center;justify-content:center}
.placeholder{position:absolute;left:17px;top:5px;font-size:3.4px;color:var(--muted)}
.label{position:absolute;left:17px;top:2.3px;font-size:2.5px;color:var(--muted)}
.value{position:absolute;left:17px;top:6.8px;font-size:3.8px}
.dots{position:absolute;left:17px;top:6.6px;font-size:4.6px;letter-spacing:.2px;line-height:1}
.caret{display:inline-block;width:.4px;height:4.2px;background:var(--ink);vertical-align:middle}
.field-tool{position:absolute;top:4.5px}
.tool-divider{position:absolute;right:11px;top:3px;width:.4px;height:8px;background:var(--line)}
.btn{position:absolute;right:17.5px;height:10.5px;border-radius:6px;color:#fff;font-weight:600;font-size:3.4px;letter-spacing:.2px;display:flex;align-items:center;justify-content:center;background:var(--green)}
.btn.next{width:25.5px;top:49.5px}
.btn.login{width:27px;top:82.5px}
.btn.off{background:var(--disabled);color:#eee}
.forgot{position:absolute;left:17.5px;top:86px;font-size:3.4px;font-weight:500;color:var(--blue)}
.db-row{position:absolute;left:17.5px;top:27px;display:flex;align-items:center;font-size:3.6px;gap:3px}
.db-row .divider{width:.4px;height:6px;background:var(--line);margin:0 1.5px}
.db-row strong{font-weight:600}
.notice{height:10.5px;background:#f6f6f6;border-top:.5px solid #eee;font-size:2.6px;display:flex;align-items:center;justify-content:center;color:#555;border-radius:0 0 2px 2px}
.notice strong{font-weight:600;color:var(--ink)}
.site-footer{position:absolute;left:0;right:0;top:188.5px;text-align:center}
.site-links{font-size:2.9px;color:#333;font-weight:500}
.site-links span{margin:0 2px;color:#aaa}
.copyright{margin-top:3.2px;font-size:2.8px;color:var(--muted)}
</style>
</head>
<body>
<svg width="0" height="0" style="position:absolute" aria-hidden="true">
  <defs>
    <symbol id="i-lock" viewBox="0 0 12 14"><rect x="1" y="6" width="10" height="8" rx="1.5" fill="#3a78c2"/><path d="M3.2 6V4.2a2.8 2.8 0 0 1 5.6 0V6" fill="none" stroke="#3a78c2" stroke-width="1.4"/></symbol>
    <symbol id="i-db" viewBox="0 0 14 12"><rect x="1" y="1" width="12" height="4.2" rx="1.2" fill="none" stroke="#444" stroke-width="1.1"/><rect x="1" y="6.8" width="12" height="4.2" rx="1.2" fill="none" stroke="#444" stroke-width="1.1"/></symbol>
    <symbol id="i-user" viewBox="0 0 12 12"><circle cx="6" cy="4" r="2.6" fill="none" stroke="#444" stroke-width="1"/><path d="M1.5 11.2a4.5 4.5 0 0 1 9 0z" fill="none" stroke="#444" stroke-width="1"/></symbol>
    <symbol id="i-key" viewBox="0 0 12 12"><circle cx="7.8" cy="4.2" r="2.6" fill="none" stroke="#444" stroke-width="1"/><path d="M5.9 6.1 1.5 10.5M2.8 9.2l1.2 1.2" fill="none" stroke="#444" stroke-width="1"/></symbol>
    <symbol id="i-x" viewBox="0 0 10 10"><path d="M1.5 1.5l7 7M8.5 1.5l-7 7" stroke="#777" stroke-width="1"/></symbol>
    <symbol id="i-eye-off" viewBox="0 0 12 10"><path d="M1 5s2-3.5 5-3.5S11 5 11 5 9 8.5 6 8.5 1 5 1 5z" fill="none" stroke="#777" stroke-width=".9"/><circle cx="6" cy="5" r="1.5" fill="none" stroke="#777" stroke-width=".9"/><path d="M2 9 10 1" stroke="#777" stroke-width=".9"/></symbol>
    <symbol id="i-back" viewBox="0 0 12 8"><path d="M11 4H1.5M4.5 1 1.5 4l3 3" fill="none" stroke="#888" stroke-width=".9"/></symbol>
  </defs>
</svg>

<main class="board">

  <!-- Step 1: empty database -->
  <section class="screen step-one" style="left:21.5px;top:21.5px">
    <header class="screen-header"><div class="brand">MERIDIAN RECORDS</div></header>
    <div class="card">
      <nav class="tabs">
        <div class="tab active"><svg width="5" height="6"><use href="#i-lock"/></svg></div>
        <div class="tab"><span class="tab-dot"></span></div>
        <div class="tab"><span class="tab-square"></span></div>
        <div class="tab"><span class="tab-dot dark"></span></div>
      </nav>
      <div class="card-body">
        <h1 class="title">Classic Login</h1>
        <div class="field" style="top:26.5px">
          <div class="field-icon"><svg width="5" height="4.5"><use href="#i-db"/></svg></div>
          <span class="placeholder">Database</span>
        </div>
        <div class="btn next off">NEXT</div>
      </div>
      <p class="notice">All activity on this site is being recorded. Your IP Address is being saved as '<strong>192.168.168.134</strong>'.</p>
    </div>
    <footer class="site-footer">
      <div class="site-links">Privacy<span>•</span>Remote Support<span>•</span>Contact Us</div>
      <div class="copyright">Copyright 2007-2024 Meridian Records Ltd</div>
    </footer>
  </section>

  <!-- Step 1: database entered -->
  <section class="screen step-one" style="left:414px;top:21.5px">
    <header class="screen-header"><div class="brand">MERIDIAN RECORDS</div></header>
    <div class="card">
      <nav class="tabs">
        <div class="tab active"><svg width="5" height="6"><use href="#i-lock"/></svg></div>
        <div class="tab"><span class="tab-dot"></span></div>
        <div class="tab"><span class="tab-square"></span></div>
        <div class="tab"><span class="tab-dot dark"></span></div>
      </nav>
      <div class="card-body">
        <h1 class="title">Classic Login</h1>
        <div class="field focused" style="top:26.5px">
          <div class="field-icon"><svg width="5" height="4.5"><use href="#i-db"/></svg></div>
          <span class="label">Database</span>
          <span class="value">ABC12345<span class="caret"></span></span>
          <svg class="field-tool" style="right:5px" width="4.5" height="4.5"><use href="#i-x"/></svg>
        </div>
        <div class="btn next">NEXT</div>
      </div>
      <p class="notice">All activity on this site is being recorded. Your IP Address is being saved as '<strong>192.168.168.134</strong>'.</p>
    </div>
    <footer class="site-footer">
      <div class="site-links">Privacy<span>•</span>Remote Support<span>•</span>Contact Us</div>
      <div class="copyright">Copyright 2007-2024 Meridian Records Ltd</div>
    </footer>
  </section>

  <!-- Step 1: invalid database -->
  <section class="screen step-one" style="left:807px;top:21.5px">
    <header class="screen-header"><div class="brand">MERIDIAN RECORDS</div></header>
    <div class="card">
      <nav class="tabs">
        <div class="tab active"><svg width="5" height="6"><use href="#i-lock"/></svg></div>
        <div class="tab"><span class="tab-dot"></span></div>
        <div class="tab"><span class="tab-square"></span></div>
        <div class="tab"><span class="tab-dot dark"></span></div>
      </nav>
      <div class="card-body">
        <h1 class="title">Classic Login</h1>
        <span class="error">Invalid database!</span>
        <div class="field invalid" style="top:26.5px">
          <div class="field-icon"><svg width="5" height="4.5"><use href="#i-db"/></svg></div>
          <span class="label">Database</span>
          <span class="value">ABC12345XYZ</span>
          <svg class="field-tool" style="right:5px" width="4.5" height="4.5"><use href="#i-x"/></svg>
        </div>
        <div class="btn next">NEXT</div>
      </div>
      <p class="notice">All activity on this site is being recorded. Your IP Address is being saved as '<strong>192.168.168.134</strong>'.</p>
    </div>
    <footer class="site-footer">
      <div class="site-links">Privacy<span>•</span>Remote Support<span>•</span>Contact Us</div>
      <div class="copyright">Copyright 2007-2024 Meridian Records Ltd</div>
    </footer>
  </section>

  <!-- Step 2: empty credentials -->
  <section class="screen step-two" style="left:21.5px;top:252px">
    <header class="screen-header"><div class="brand">MERIDIAN RECORDS</div></header>
    <div class="card">
      <nav class="tabs">
        <div class="tab active"><svg width="5" height="6"><use href="#i-lock"/></svg></div>
        <div class="tab"><span class="tab-dot"></span></div>
        <div class="tab"><span class="tab-square"></span></div>
        <div class="tab"><span class="tab-dot dark"></span></div>
      </nav>
      <div class="card-body">
        <h1 class="title">Classic Login</h1>
        <div class="db-row"><svg width="5" height="3.5"><use href="#i-back"/></svg><span class="divider"></span><svg width="5" height="4.5"><use href="#i-db"/></svg><span>Database: <strong>ABC12345</strong></span></div>
        <div class="field" style="top:41.5px">
          <div class="field-icon"><svg width="4.5" height="4.5"><use href="#i-user"/></svg></div>
          <span class="placeholder">Username</span>
        </div>
        <div class="field" style="top:59.5px">
          <div class="field-icon"><svg width="4.5" height="4.5"><use href="#i-key"/></svg></div>
          <span class="placeholder">Password</span>
          <svg class="field-tool" style="right:5px" width="5" height="4.5"><use href="#i-eye-off"/></svg>
        </div>
        <span class="forgot">Forgot Password?</span>
        <div class="btn login off">LOGIN</div>
      </div>
      <p class="notice">All activity on this site is being recorded. Your IP Address is being saved as '<strong>192.168.168.134</strong>'.</p>
    </div>
    <footer class="site-footer">
      <div class="site-links">Privacy<span>•</span>Remote Support<span>•</span>Contact Us</div>
      <div class="copyright">Copyright 2007-2024 Meridian Records Ltd</div>
    </footer>
  </section>

  <!-- Step 2: credentials entered -->
  <section class="screen step-two" style="left:414px;top:252px">
    <header class="screen-header"><div class="brand">MERIDIAN RECORDS</div></header>
    <div class="card">
      <nav class="tabs">
        <div class="tab active"><svg width="5" height="6"><use href="#i-lock"/></svg></div>
        <div class="tab"><span class="tab-dot"></span></div>
        <div class="tab"><span class="tab-square"></span></div>
        <div class="tab"><span class="tab-dot dark"></span></div>
      </nav>
      <div class="card-body">
        <h1 class="title">Classic Login</h1>
        <div class="db-row"><svg width="5" height="3.5"><use href="#i-back"/></svg><span class="divider"></span><svg width="5" height="4.5"><use href="#i-db"/></svg><span>Database: <strong>ABC12345</strong></span></div>
        <div class="field" style="top:41.5px">
          <div class="field-icon"><svg width="4.5" height="4.5"><use href="#i-user"/></svg></div>
          <span class="label">Username</span>
          <span class="value">JohnDoe123</span>
          <svg class="field-tool" style="right:5px" width="4.5" height="4.5"><use href="#i-x"/></svg>
        </div>
        <div class="field focused" style="top:59.5px">
          <div class="field-icon"><svg width="4.5" height="4.5"><use href="#i-key"/></svg></div>
          <span class="label">Password</span>
          <span class="dots">●●●<span class="caret"></span></span>
          <svg class="field-tool" style="right:18px" width="5" height="4.5"><use href="#i-eye-off"/></svg>
          <span class="tool-divider" style="right:13.5px"></span>
          <svg class="field-tool" style="right:5px" width="4.5" height="4.5"><use href="#i-x"/></svg>
        </div>
        <span class="forgot">Forgot Password?</span>
        <div class="btn login">LOGIN</div>
      </div>
      <p class="notice">All activity on this site is being recorded. Your IP Address is being saved as '<strong>192.168.168.134</strong>'.</p>
    </div>
    <footer class="site-footer">
      <div class="site-links">Privacy<span>•</span>Remote Support<span>•</span>Contact Us</div>
      <div class="copyright">Copyright 2007-2024 Meridian Records Ltd</div>
    </footer>
  </section>

  <!-- Step 2: invalid credentials -->
  <section class="screen step-two" style="left:807px;top:252px">
    <header class="screen-header"><div class="brand">MERIDIAN RECORDS</div></header>
    <div class="card">
      <nav class="tabs">
        <div class="tab active"><svg width="5" height="6"><use href="#i-lock"/></svg></div>
        <div class="tab"><span class="tab-dot"></span></div>
        <div class="tab"><span class="tab-square"></span></div>
        <div class="tab"><span class="tab-dot dark"></span></div>
      </nav>
      <div class="card-body">
        <h1 class="title">Classic Login</h1>
        <span class="error">Invalid username and/or password!</span>
        <div class="db-row"><svg width="5" height="3.5"><use href="#i-back"/></svg><span class="divider"></span><svg width="5" height="4.5"><use href="#i-db"/></svg><span>Database: <strong>ABC12345</strong></span></div>
        <div class="field" style="top:41.5px">
          <div class="field-icon"><svg width="4.5" height="4.5"><use href="#i-user"/></svg></div>
          <span class="label">Username</span>
          <span class="value">JohnDoe123</span>
          <svg class="field-tool" style="right:5px" width="4.5" height="4.5"><use href="#i-x"/></svg>
        </div>
        <div class="field focused" style="top:59.5px">
          <div class="field-icon"><svg width="4.5" height="4.5"><use href="#i-key"/></svg></div>
          <span class="label">Password</span>
          <span class="dots">●●●<span class="caret"></span></span>
          <svg class="field-tool" style="right:18px" width="5" height="4.5"><use href="#i-eye-off"/></svg>
          <span class="tool-divider" style="right:13.5px"></span>
          <svg class="field-tool" style="right:5px" width="4.5" height="4.5"><use href="#i-x"/></svg>
        </div>
        <span class="forgot">Forgot Password?</span>
        <div class="btn login">LOGIN</div>
      </div>
      <p class="notice">All activity on this site is being recorded. Your IP Address is being saved as '<strong>192.168.168.134</strong>'.</p>
    </div>
    <footer class="site-footer">
      <div class="site-links">Privacy<span>•</span>Remote Support<span>•</span>Contact Us</div>
      <div class="copyright">Copyright 2007-2024 Meridian Records Ltd</div>
    </footer>
  </section>

</main>
</body>
</html>
```